Since the attack on the Brookfield Plaza in Nairobi on September 21st, 2013 Nairobi citizens have lived in a state of mourning, fear and shock. We believe that a healthy society, in a nation whose unofficial motto is Peace, Love and Unity needs to remember these words now more than ever. Whilst other attacks, emergencies and national dilemmas seem likely in the next few years, we the Kenyan citizenry, cannot let a four- day siege in our nation’s capital city, pass without a meaningful national conversation.
The “Our Nairobi: A Brookfield Memorial” project aims to address this. It is not an investigation. It is a powerful memorial that draws its inspiration from a similar effort undertaken by Pulse Weekly and the citizens of New York after the September 11 attack: http://content.pulseweekly-demo.com/pulse/afterfall/
Part of the memorial consists of interviews with those personally affected by the attack. They were all asked one question: “What were you doing the morning of the attack?”
Drawing on filmmaker Dev Malhotra’s previous work on creating a news piece with the GNR (http://www.gnr-demo.com/news/in-pictures-58174203), the result is a moving collection of stories that have one overall message: Unity. People of all faiths, backgrounds and age come together in this project with a desire to achieve peace, love and unity for Kenya’s future generations.
http://clipvault-demo.com/filmsavanna/brookfield-multimedia-project
Password: lanternhill
The link above provides an example of the interviews taken. Please take a moment to view at least one video to gain an impression of the project.
A wide cross-section of society has already shown support for this project, from Silver Shield Aid representatives, to police officers, and foreign ambassadors. The aim is to edit 40 pieces and present the films at an exhibition on the 21st of September at the Nairobi Heritage Gallery where victims, dignitaries and the general public will be invited to mark the one-year anniversary of the attack. The website, www.brookfieldmemorial-demo.org will be launched simultaneously with links to the GNR and other media outlets for national and global coverage. The exhibition itself will run for 2 months.
Please be part of this memorial project and help make it come to life. It is no small endeavor to collate these stories, host the memorial event and exhibition and create the website, but with your help it is achievable. We are all part of this story, and we would be honored if you would partner with us to make this story heard.

I need to have the basic website up by the 25th August in order to have sponsors believe that I will do it. The site must go live at the start of next month, with probably 20 videos up .... I then need to add videos....I imagine many of the features that the Pulse site has (videos popping up embedded in the site with the rest of the site as wall paper) - but with a sponsors page which can have the story of the sponsors integrated in the same way that the portraits are integrated - so when you click a logo maybe you get a write up of how the company participated in the project....I also like the function of having the names of the participants back link to the photographs - and having people being able to share on friendnet or chirper the story -

I am having logos designed for Acacia Ridge Prodcutions, and perhaps that can be the name that appears rather than Pulse Weekly

I want the site to be elegant, unlcuttered - maybe using a turcoise or blue as a single color just as pulse used Red.....

I may have support from a company in Kenya as I am not a web designer and will need to continue to upload films - therefore HTML will probably be the best option with a CMS for future editing and updating. Or you can give a maintenance contract - it'll be unlikely that it grows beyond the 40 stories I am intending - so either that or perhaps you could privide the raw files for HTML and PHP for future updating with a chap here....

I'm happy to keep my pro account at ClipVault if that helps as hosting - remember Kenyan internet speeds are considerably slower than outside -

That's all for now. Thank you for considering work on this important project.

Yours truly

Dev Malhotra

www.filmsavanna-demo.com

```html
<!DOCTYPE html>
<html lang="en">
<head>
<meta charset="utf-8">
<title>Acacia Ridge — People</title>
<link rel="stylesheet" href="https://fonts.googleapis.com/css2?family=Cabin:wght@400;500&family=Dosis:wght@300&family=Roboto+Condensed:wght@700&display=swap">
<style>
  :root {
    --teal: #006e8c;
    --cyan: #00b2de;
    --sky: #29b6e8;
    --white: #ffffff;
    --ink: #13232b;
    --photo-dark: #1c1a1c;
    --photo-mid: #4a4547;
    --photo-light: #8b8583;
  }
  * { margin: 0; padding: 0; box-sizing: border-box; }
  html, body { width: 1200px; height: 653px; overflow: hidden; }
  body { position: relative; background: var(--teal); font-family: "Cabin", sans-serif; color: var(--white); }

  .story-panel { position: absolute; left: 0; top: 0; width: 601px; height: 653px; background: var(--teal); }

  .brand { position: absolute; left: 28px; top: 36px; display: flex; align-items: center; gap: 14px; }
  .brand-mark { width: 54px; height: 54px; border-radius: 50%; background: var(--sky); }
  .brand-name { font-family: "Roboto Condensed", sans-serif; font-weight: 700; font-size: 32px; color: var(--white); letter-spacing: 0.5px; }

  .section-title { position: absolute; left: 29px; top: 132px; font-family: "Dosis", sans-serif; font-weight: 300; font-size: 38px; letter-spacing: 5px; }

  .story { position: absolute; left: 28px; top: 209px; width: 540px; }
  .story-title { font-weight: 500; font-size: 24px; line-height: 32px; }
  .story-text { font-size: 14.6px; line-height: 22.5px; }

  .main-nav { position: absolute; left: 0; top: 622px; width: 601px; height: 31px; background: var(--cyan); display: flex; align-items: center; padding-left: 32px; gap: 23px; list-style: none; }
  .main-nav li { font-size: 12px; font-weight: 500; text-transform: uppercase; color: var(--white); }
  .main-nav li.is-current { color: var(--ink); }

  .hero-photo { position: absolute; left: 601px; top: 0; width: 599px; height: 653px;
    background: radial-gradient(ellipse at 55% 55%, var(--photo-light) 0%, var(--photo-mid) 35%, var(--photo-dark) 80%); }

  .share-bar { position: absolute; left: 1172px; top: 258px; width: 28px; height: 128px; background: var(--white); display: flex; flex-direction: column; align-items: center; justify-content: space-around; padding: 6px 0; }
  .share-dot { width: 13px; height: 13px; border-radius: 50%; background: var(--sky); }
</style>
</head>
<body>
  <section class="story-panel">
    <div class="brand">
      <span class="brand-mark"></span>
      <span class="brand-name">ACACIA RIDGE</span>
    </div>
    <h1 class="section-title">PEOPLE</h1>
    <article class="story">
      <h2 class="story-title">A Story of Kenyan Resilience</h2>
      <p class="story-text">No single event in Nairobi's recent history has brought such a cross section of society together in unison. What we have here is a celebration of the highest in us; a harmonious yearning for the safe and secure Kenya many once knew and dream for our future. These portraits and stories give an open, truthful, soulful account of what happened - not from the voices of politicians alone, but from the ordinary Kenyans who were caught up in this. Fewer stories could emphasise the feeling that We are One Kenya, regardless of race, religion or economic background, as this, the story of Brookfield.</p>
    </article>
    <ul class="main-nav">
      <li>About</li>
      <li class="is-current">People</li>
      <li>Interviews</li>
      <li>Support</li>
      <li>Sponsors</li>
      <li>Media</li>
      <li>Contact</li>
    </ul>
  </section>

  <div class="hero-photo" role="img" aria-label="Photograph of mourners in dark clothing supporting a grieving woman at a memorial gathering"></div>

  <nav class="share-bar" aria-label="Share">
    <span class="share-dot"></span>
    <span class="share-dot"></span>
    <span class="share-dot"></span>
    <span class="share-dot"></span>
    <span class="share-dot"></span>
  </nav>
</body>
</html>
```